Web Design Business Card

I need a new business card designed, we recently rebranded and I need to get a fresh design to match our new logo, colours and branding.

Details:

Dorin Vaskel | Founder & CEO
Address: 7 Fernbrook Lane, #14-05 Maralune Crest, Singapore 318457
Tel: +65 93640281
Web: www.plumtrove.com.sg
hello@plumtrove.com.sg

I've attached my old card as well

Industry/Entity Type

Business

Requirements
Must have
• Front and Back
Interesting use of logo
Correct use of colour scheme

```html
<!DOCTYPE html>
<html lang="en">
<head>
<meta charset="utf-8">
<title>Plumtrove Business Card</title>
<link rel="stylesheet" href="https://fonts.googleapis.com/css2?family=Questrial&display=swap">
<style>
  :root {
    --backdrop: #e9e7e4;
    --card-light: #ffffff;
    --card-shade: #e4e4e4;
    --brand-blue: #2a9fd3;
    --ink: #5a4f4a;
    --card-shadow: rgba(40, 30, 20, 0.22);
  }
  * { box-sizing: border-box; margin: 0; padding: 0; }
  html, body {
    width: 1200px;
    height: 900px;
    overflow: hidden;
    background: var(--backdrop);
    font-family: "Questrial", "Century Gothic", sans-serif;
    color: var(--ink);
  }
  .canvas {
    position: relative;
    width: 1200px;
    height: 900px;
  }
  .card {
    position: absolute;
    left: 280px;
    width: 640px;
    height: 366px;
    border-radius: 22px;
    background: radial-gradient(ellipse at 35% 20%, var(--card-light) 0%, #f6f6f6 45%, var(--card-shade) 100%);
    box-shadow: 0 10px 28px var(--card-shadow);
    overflow: hidden;
  }
  .card--back { top: 66px; }
  .card--front { top: 468px; }

  /* back: brand lockup bottom-left */
  .brand-lockup {
    position: absolute;
    left: 36px;
    bottom: 34px;
    display: flex;
    align-items: center;
    gap: 12px;
  }
  .brand-lockup__dot {
    width: 40px;
    height: 40px;
    border-radius: 50%;
    background: var(--brand-blue);
  }
  .brand-lockup__name {
    font-size: 34px;
    letter-spacing: 0.5px;
    color: var(--ink);
  }

  /* front */
  .brand-disc {
    position: absolute;
    top: 30px;
    right: 44px;
    width: 218px;
    height: 218px;
    border-radius: 50%;
    background: linear-gradient(180deg, #2a9fd3 0%, #4aa8d6 100%);
    display: flex;
    align-items: center;
    justify-content: center;
  }
  .brand-disc__name {
    font-size: 32px;
    color: #ffffff;
    letter-spacing: 0.5px;
  }
  .holder {
    position: absolute;
    left: 52px;
    top: 96px;
  }
  .holder__name {
    font-size: 27px;
    letter-spacing: 0.5px;
    color: var(--ink);
  }
  .holder__role {
    margin: 4px 0 0 42px;
    font-size: 15px;
    color: var(--brand-blue);
  }
  .contact {
    position: absolute;
    left: 52px;
    bottom: 40px;
    list-style: none;
    font-size: 17px;
    line-height: 30px;
    color: var(--ink);
  }
  .contact__label {
    display: inline-block;
    width: 26px;
    color: var(--brand-blue);
  }
  .contact__line2 {
    display: block;
    padding-left: 212px;
    line-height: 18px;
  }
  .contact__item--address { line-height: 22px; margin-top: 6px; }
</style>
</head>
<body>
  <main class="canvas">
    <section class="card card--back" aria-label="Card back">
      <div class="brand-lockup">
        <span class="brand-lockup__dot"></span>
        <span class="brand-lockup__name">plumtrove</span>
      </div>
    </section>

    <section class="card card--front" aria-label="Card front">
      <div class="brand-disc">
        <span class="brand-disc__name">plumtrove</span>
      </div>

      <div class="holder">
        <p class="holder__name">Dorin Vaskel</p>
        <p class="holder__role">Founder &amp; CEO</p>
      </div>

      <ul class="contact">
        <li><span class="contact__label">T:</span>+65 93640281</li>
        <li><span class="contact__label">W:</span>www.plumtrove.com.sg</li>
        <li><span class="contact__label">E:</span>hello@plumtrove.com.sg</li>
        <li class="contact__item--address"><span class="contact__label">A:</span>Fernbrook Lane, #14-05 Maralune Crest
          <span class="contact__line2">Singapore 318457</span></li>
      </ul>
    </section>
  </main>
</body>
</html>
```